An e-flyer for an exotic car and fine wine club.

This is the first meeting of Brixley Motor Society and includes several businesses. Their logos should be featured at the bottom. It should be sleek, elegant and simple featuring a photo of an Corvane Halder T7 as well as my logo (I will provide photos). The flyer needs to look professional and appeal to billionaires.
The text should read:
Brixley Motor society presents
Swift Wheels and Vintage Pours (but not while driving)
Hosted by Wrenfold Vault Rooms
Bring your best car(s) and join us to enjoy the party with sommelier selected wines, the best classic and modern cars and hors d'oeuvre catered by Dunmore's Shellfish Bar. Live DJ.
August 26th 3-6 p.m.
This event is gratis.
RSVP to nora@brixleymotorsociety.example for address and details

Target Market(s)
Very wealthy exotic car owners
Industry/Entity Type
Car Club, Fine Wines.
Requirements
Must have
- Style, panache, elegance, sleekness, simplicity. I like the idea of a black or dark flyer with a consistent color scheme.
Nice to have
- I want the flyer to be simple and sleek, feature an Corvane Halder T7 as the eye catcher, Brixley Motor Society logo featured prominently on the top, and the other business logos on the bottom.
Should not have
- It must not be too noisy or busy.

```html
<!DOCTYPE html>
<html lang="en">
<head>
<meta charset="utf-8">
<title>Swift Wheels &amp; Vintage Pours — Brixley Motor Society</title>
<link rel="stylesheet" href="https://fonts.googleapis.com/css2?family=Arimo:wght@400;700&family=Oswald:wght@500&family=Rye&display=swap">
<style>
  :root {
    --paper: #ffffff;
    --navy: #0f1b2a;
    --wine-deep: #7a0c14;
    --wine-mid: #8e1a24;
    --wine-light: #a0303b;
    --amp-red: #e0242b;
    --ink: #000000;
    --text-light: #ffffff;
    --car-red: #e8403c;
  }
  * { margin: 0; padding: 0; box-sizing: border-box; }
  html, body { width: 849px; height: 1200px; overflow: hidden; background: var(--paper); }
  .flyer {
    position: relative; width: 849px; height: 1200px; overflow: hidden;
    font-family: "Arimo", Arial, sans-serif; color: var(--text-light);
  }
  .masthead { position: absolute; left: 0; top: 0; width: 849px; height: 210px; background: var(--paper); }
  .club-name {
    position: absolute; left: 390px; top: 92px; width: 272px; text-align: center;
    font-weight: 700; font-size: 22px; line-height: 30px; letter-spacing: 4px; color: var(--navy);
  }
  .club-rule { position: absolute; left: 389px; top: 206px; width: 274px; height: 3px; background: #333; }
  .stage {
    position: absolute; left: 0; top: 210px; width: 849px; height: 990px;
    background:
      linear-gradient(172deg, transparent 0 40%, rgba(160,48,59,.35) 48%, transparent 56%),
      linear-gradient(176deg, var(--wine-mid) 0%, var(--wine-deep) 30%, var(--wine-light) 55%, var(--wine-deep) 75%, var(--wine-mid) 100%);
  }
  .hero-car {
    position: absolute; left: 45px; top: 1000px; width: 705px; height: 185px;
    border-radius: 160px 200px 40px 40px;
    background: radial-gradient(ellipse at 50% 40%, var(--car-red), #c52a28 70%, rgba(122,12,20,0) 100%);
  }
  .presents {
    position: absolute; left: 440px; top: 220px; font-size: 11px; font-weight: 700;
    letter-spacing: 10.5px; color: var(--text-light);
  }
  .title { font-family: "Rye", Georgia, serif; color: var(--text-light); position: absolute; line-height: 1; white-space: nowrap; }
  .title-swift { left: 150px; top: 238px; font-size: 100px; }
  .title-wheels { left: 250px; top: 345px; font-size: 86px; }
  .title-vintage { left: 150px; top: 455px; font-size: 86px; }
  .title-pours { left: 290px; top: 555px; font-size: 96px; }
  .title-amp {
    position: absolute; left: 525px; top: 428px; font-family: Georgia, serif; font-style: italic;
    font-size: 70px; color: var(--amp-red); line-height: 1;
  }
  .tagline { position: absolute; left: 345px; width: 352px; text-align: center; font-weight: 700; color: var(--text-light); }
  .tagline-drive { top: 657px; font-size: 20px; }
  .tagline-host { top: 689px; font-size: 17.5px; }
  .rule { position: absolute; left: 345px; width: 352px; height: 2px; background: var(--ink); }
  .rule-a { top: 681px; }
  .rule-b { top: 713px; }
  .details {
    position: absolute; left: 391px; top: 719px; width: 270px; font-size: 16px; line-height: 21px;
    text-align: justify; color: var(--text-light);
  }
  .live { position: absolute; left: 391px; top: 829px; width: 254px; text-align: center; font-weight: 700; font-size: 16px; }
  .date-box {
    position: absolute; left: 389px; top: 852px; width: 274px; height: 39px; background: var(--ink);
    font-family: "Oswald", "Arial Narrow", sans-serif; font-weight: 500; font-size: 27px; line-height: 39px;
    text-align: center; color: var(--text-light);
  }
  .date-box sup { font-size: 13px; vertical-align: 12px; line-height: 0; }
  .rsvp { position: absolute; left: 498px; top: 898px; font-size: 9px; line-height: 14px; color: var(--text-light); }
  .partners { position: absolute; left: 503px; top: 950px; width: 140px; display: flex; gap: 14px; align-items: center; }
  .partner { font-weight: 700; font-size: 8px; line-height: 10px; color: var(--text-light); text-align: center; }
</style>
</head>
<body>
<main class="flyer">
  <header class="masthead">
    <div class="club-name">BRIXLEY<br>MOTOR SOCIETY</div>
    <div class="club-rule"></div>
  </header>

  <section class="stage"></section>

  <div class="hero-car" role="img" aria-label="Photo of a red Corvane Halder T7 classic coupe in three-quarter front view"></div>

  <p class="presents">PRESENTS</p>

  <h1 aria-label="Swift Wheels and Vintage Pours">
    <span class="title title-swift">swift</span>
    <span class="title title-wheels">wheels</span>
    <span class="title-amp">&amp;</span>
    <span class="title title-vintage">vintage</span>
    <span class="title title-pours">pours</span>
  </h1>

  <p class="tagline tagline-drive">BUT NOT WHILE DRIVING</p>
  <div class="rule rule-a"></div>
  <p class="tagline tagline-host">HOSTED BY WRENFOLD VAULT ROOMS</p>
  <div class="rule rule-b"></div>

  <p class="details">Bring your best car(s) and join us to enjoy the party with sommelier selected wines, the best classic and modern cars and hors d'oeuvre catered by Dunmore's Shellfish Bar.</p>
  <p class="live">Live DJ.</p>

  <div class="date-box">AUGUST 26<sup>TH</sup> 3-6 P.M.</div>

  <p class="rsvp">THIS EVENT IS GRATIS.<br>RSVP to nora@brixleymotorsociety.example<br>for address and details</p>

  <div class="partners">
    <span class="partner">WRENFOLD<br>VAULT</span>
    <span class="partner">MARLOWE<br>WINE STORE</span>
  </div>
</main>
</body>
</html>
```